Company Business Card, for Harborveldt.com Floating homes and Marinas

To design a new great looking business card that follows some how the theme of our business and website. Harborveldt.com

I have attached our logo and a copy of our existing card (boring)

   We appreciate everyones efforts so far there are some very interesting designs. We are thinking that our company is more than just a Marina manufacturer, we build many different floating products and we would like our card to show case those products. There has been one card that has done this, and we are leaning towards that design. We prefer that our logo and company name are proportional on the card, and our mission statement be also shown. Thank you                                

                                   

 We do like your designs, on the back of the card  we want to show all 6 different product types as shown on the front of our website.

                                   

Sorry some designers have the images on the front, and that is okay as well. We just want on the card all 6 areas that we manufacture.

• Must have a new look, maybe nautical, following the theme of what our company manufactures.

Logo
Company name: Consolidated Pontoon Dockworks Group, Inc.

Website: www.HarborVeldt.com

Employee name & title

Mission statement: "Craftsmanship is the keel that carries every voyage"

Our Address: 4718 Quillan Avenue, Delta, B.C. Canada, V3K 2R7

• Colour and unique presentation,

```html
<!DOCTYPE html>
<html lang="en">
<head>
<meta charset="utf-8">
<title>Consolidated Pontoon Dockworks Group — Business Cards</title>
<link href="https://fonts.googleapis.com/css2?family=Jost:wght@400;500;600&display=swap" rel="stylesheet">
<style>
  :root {
    --page: #ffffff;
    --card: #ffffff;
    --ink: #111418;
    --brand-blue: #1f5fa8;
    --contact-blue: #2a5c96;
    --sea-deep: #0b3f7a;
    --sea-mid: #1f7fbf;
    --sea-bright: #2fb3c9;
    --sea-teal: #1f6f86;
    --logo: #ffffff;
    --logo-soft: rgba(255,255,255,0.85);
  }
  * { margin: 0; padding: 0; box-sizing: border-box; }
  html, body {
    width: 1200px; height: 900px; overflow: hidden;
    background: var(--page);
    font-family: "Jost", "Futura", sans-serif;
  }
  .sheet { position: relative; width: 1200px; height: 900px; }
  .card { position: absolute; width: 285px; height: 185px; }
  .card--front {
    top: 250px;
    background: var(--card);
    box-shadow: 0 2px 10px rgba(0,0,0,0.10);
  }
  .card--back { top: 458px; height: 184px; overflow: hidden; }
  .col-1 { left: 124px; }
  .col-2 { left: 450px; }
  .col-3 { left: 776px; }

  .person {
    position: absolute; left: 25px; top: 30px;
    font-size: 8px; font-weight: 500; line-height: 10px; color: var(--ink);
  }
  .person__title {
    display: block; font-size: 6.2px; font-weight: 400; color: var(--contact-blue);
  }
  .company {
    position: absolute; left: 25px; top: 81px;
    font-size: 9.4px; font-weight: 500; line-height: 11px;
    color: var(--ink); text-transform: uppercase; letter-spacing: 0.1px;
  }
  .mission {
    position: absolute; left: 25px; top: 104px;
    font-size: 6px; font-weight: 600; color: var(--brand-blue); white-space: nowrap;
  }
  .contact {
    position: absolute; left: 25px; top: 130px;
    font-size: 6.2px; line-height: 11px; color: var(--contact-blue);
  }
  .contact b { font-weight: 600; color: var(--brand-blue); }
  .contact .web { font-weight: 600; }
  .address {
    position: absolute; left: 131px; top: 130px;
    font-size: 6.2px; line-height: 11px; color: var(--contact-blue);
  }

  .sea { position: absolute; inset: 0; }
  .sea--foam {
    background:
      radial-gradient(ellipse at 75% 30%, rgba(80,200,215,0.7), transparent 55%),
      radial-gradient(ellipse at 20% 80%, rgba(5,40,95,0.8), transparent 60%),
      linear-gradient(135deg, var(--sea-deep), var(--sea-mid) 55%, #1a8fb8);
  }
  .sea--shallow {
    background:
      radial-gradient(ellipse at 60% 90%, rgba(60,200,200,0.6), transparent 55%),
      linear-gradient(160deg, #1a6fd0, var(--sea-mid) 45%, var(--sea-bright));
  }
  .sea--ripple {
    background:
      radial-gradient(ellipse at 85% 40%, rgba(40,140,150,0.7), transparent 55%),
      linear-gradient(120deg, #123f78, #1d5a8e 45%, var(--sea-teal));
  }
  .wordmark {
    position: absolute; left: 0; right: 0; top: 80px;
    text-align: center;
    font-size: 18px; font-weight: 600; letter-spacing: 2px;
    color: var(--logo);
  }
  .products {
    position: absolute; left: 0; right: 0; bottom: 14px;
    text-align: center; white-space: nowrap;
    font-size: 5.6px; font-weight: 500; letter-spacing: 0.3px;
    color: var(--logo-soft); text-transform: uppercase;
  }
</style>
</head>
<body>
<main class="sheet">

  <section class="card card--front col-1">
    <p class="person">Marcus Ellery<span class="person__title">Sales Manager</span></p>
    <h2 class="company">Consolidated Pontoon<br>Dockworks Group, Inc.</h2>
    <p class="mission">“Craftsmanship is the keel that carries every voyage”</p>
    <p class="contact"><b>T</b> 604 555 0147<br><b>E</b> Info@HarborVeldt.com<br><span class="web">www.HarborVeldt.com</span></p>
    <p class="address">4718 Quillan Avenue, Delta,<br>B.C. Canada, V3K 2R7</p>
  </section>
  <section class="card card--front col-2">
    <p class="person">Marcus Ellery<span class="person__title">Sales Manager</span></p>
    <h2 class="company">Consolidated Pontoon<br>Dockworks Group, Inc.</h2>
    <p class="mission">“Craftsmanship is the keel that carries every voyage”</p>
    <p class="contact"><b>T</b> 604 555 0147<br><b>E</b> Info@HarborVeldt.com<br><span class="web">www.HarborVeldt.com</span></p>
    <p class="address">4718 Quillan Avenue, Delta,<br>B.C. Canada, V3K 2R7</p>
  </section>
  <section class="card card--front col-3">
    <p class="person">Marcus Ellery<span class="person__title">Sales Manager</span></p>
    <h2 class="company">Consolidated Pontoon<br>Dockworks Group, Inc.</h2>
    <p class="mission">“Craftsmanship is the keel that carries every voyage”</p>
    <p class="contact"><b>T</b> 604 555 0147<br><b>E</b> Info@HarborVeldt.com<br><span class="web">www.HarborVeldt.com</span></p>
    <p class="address">4718 Quillan Avenue, Delta,<br>B.C. Canada, V3K 2R7</p>
  </section>

  <section class="card card--back col-1">
    <div class="sea sea--foam" role="img" aria-label="Aerial photo of deep blue ocean with white surf foam"></div>
    <p class="wordmark">HARBORVELDT</p>
    <p class="products">Marinas · Floating Homes · Breakwaters · Boathouses · Walkways · Platforms</p>
  </section>
  <section class="card card--back col-2">
    <div class="sea sea--shallow" role="img" aria-label="Aerial photo of bright blue to turquoise shallow sea water"></div>
    <p class="wordmark">HARBORVELDT</p>
    <p class="products">Marinas · Floating Homes · Breakwaters · Boathouses · Walkways · Platforms</p>
  </section>
  <section class="card card--back col-3">
    <div class="sea sea--ripple" role="img" aria-label="Close-up photo of rippled dark blue-teal sea surface"></div>
    <p class="wordmark">HARBORVELDT</p>
    <p class="products">Marinas · Floating Homes · Breakwaters · Boathouses · Walkways · Platforms</p>
  </section>

</main>
</body>
</html>
```